Rice Package Design

I want a modern 1 kg (Bulgur) Package Design (Our products are High quality)
for the Both sides front and back-side

Opened face Size : H:28.5 cm X W:20 cm *see Atachment1-size-file.pdf

package type *see attachment The-Package-type.png

Notes :
transparent area should be a to show the rice inside (20% of the design)
* use the logo on both sides
* you can add a slogan like (The Best Logumess or Original Products)
* elements needed to use in the design are attached for both faces and the nutrition facts table
(lorem text used I want you to replace all the text after awarding you)

```html
<!DOCTYPE html>
<html lang="ar">
<head>
<meta charset="utf-8">
<title>Bulgur Package Front</title>
<link rel="stylesheet" href="https://fonts.googleapis.com/css2?family=Cairo:wght@700;800;900&family=Montserrat:wght@600;700&display=swap">
<style>
  :root{
    --stage:#a8290c;
    --green-deep:#0a5415;
    --green-mid:#17842a;
    --green-light:#3bb33f;
    --gold-dark:#a97f2e;
    --gold:#d6b05a;
    --gold-light:#f5e0a0;
    --grain-light:#ead48f;
    --grain-dark:#c4a45a;
    --red:#e3202e;
    --red-dark:#b3121f;
    --white:#ffffff;
  }
  html,body{margin:0;padding:0;}
  body{
    width:1200px;height:2321px;overflow:hidden;
    background:var(--stage);
    position:relative;
  }
  .package-front{
    position:absolute;left:100px;top:447px;
    width:1000px;height:1426px;
    box-shadow:0 14px 36px rgba(0,0,0,.45);
  }
  .package-front svg{display:block;width:100%;height:100%;}
  .arabic{font-family:'Cairo',sans-serif;}
  .latin{font-family:'Montserrat',sans-serif;}
  .headline{font-weight:900;font-size:57px;paint-order:stroke;stroke:var(--green-deep);stroke-width:4px;}
  .tagline{font-weight:800;font-size:35px;}
  .from-nature{font-weight:700;font-size:15px;letter-spacing:.3px;}
  .net-weight{font-weight:600;font-size:11.5px;}
  .new-label{font-weight:700;font-size:19px;}
  .brand-name{font-weight:800;font-size:19px;}
  .weight-badge{font-weight:800;font-size:20px;}
</style>
</head>
<body>
  <div class="package-front">
    <svg viewBox="0 0 486 693" xmlns="http://www.w3.org/2000/svg">
      <defs>
        <radialGradient id="greenField" cx="50%" cy="45%" r="70%">
          <stop offset="0" stop-color="var(--green-light)"/>
          <stop offset=".55" stop-color="var(--green-mid)"/>
          <stop offset="1" stop-color="var(--green-deep)"/>
        </radialGradient>
        <linearGradient id="goldBand" x1="0" x2="1" y1="0" y2="0">
          <stop offset="0" stop-color="var(--gold-dark)"/>
          <stop offset=".3" stop-color="var(--gold-light)"/>
          <stop offset=".7" stop-color="var(--gold)"/>
          <stop offset="1" stop-color="var(--gold-dark)"/>
        </linearGradient>
        <linearGradient id="goldText" x1="0" x2="0" y1="0" y2="1">
          <stop offset="0" stop-color="var(--gold-light)"/>
          <stop offset="1" stop-color="var(--gold)"/>
        </linearGradient>
        <radialGradient id="wheatGlow" cx="50%" cy="50%" r="50%">
          <stop offset="0" stop-color="var(--gold)" stop-opacity=".75"/>
          <stop offset=".6" stop-color="var(--gold)" stop-opacity=".35"/>
          <stop offset="1" stop-color="var(--gold)" stop-opacity="0"/>
        </radialGradient>
        <radialGradient id="grain" cx="50%" cy="40%" r="60%">
          <stop offset="0" stop-color="var(--grain-light)"/>
          <stop offset="1" stop-color="var(--grain-dark)"/>
        </radialGradient>
        <linearGradient id="bowlGreen" x1="0" x2="0" y1="0" y2="1">
          <stop offset="0" stop-color="var(--green-mid)"/>
          <stop offset="1" stop-color="var(--green-deep)"/>
        </linearGradient>
        <linearGradient id="newRed" x1="0" x2="1" y1="0" y2="1">
          <stop offset="0" stop-color="var(--red)"/>
          <stop offset="1" stop-color="var(--red-dark)"/>
        </linearGradient>
        <clipPath id="aboveBand"><rect x="0" y="0" width="486" height="449"/></clipPath>
      </defs>

      <!-- base panels -->
      <rect class="gold-band" x="0" y="0" width="486" height="693" fill="url(#goldBand)"/>
      <rect class="green-field" x="0" y="0" width="486" height="449" fill="url(#greenField)"/>

      <!-- wheat sprig areas -->
      <ellipse class="wheat-left" role="img" aria-label="Golden wheat sprig illustration"
               cx="62" cy="325" rx="62" ry="125" fill="url(#wheatGlow)"/>
      <ellipse class="wheat-right" role="img" aria-label="Golden wheat sprig illustration"
               cx="430" cy="322" rx="58" ry="118" fill="url(#wheatGlow)"/>

      <!-- bowl rim and grain window -->
      <g class="bowl-window" clip-path="url(#aboveBand)">
        <circle cx="245" cy="443" r="210" fill="url(#goldBand)"/>
        <circle cx="245" cy="448" r="190" fill="url(#grain)" role="img" aria-label="Bulgur grains seen through the window"/>
      </g>

      <!-- bowl body -->
      <path class="bowl-body" fill="url(#bowlGreen)"
            d="M34 449 H456 C452 560 400 625 318 645 L325 670 H165 L172 645 C90 625 38 560 34 449 Z"/>

      <!-- new corner -->
      <path class="new-corner" d="M0 0 H95 L0 95 Z" fill="url(#newRed)"/>
      <text class="latin new-label" x="36" y="44" fill="var(--white)" text-anchor="middle" transform="rotate(-45 36 38)">New</text>

      <!-- brand mark -->
      <circle class="brand-ring" cx="391" cy="78" r="36" fill="none" stroke="url(#goldBand)" stroke-width="4"/>
      <text class="arabic brand-name" x="391" y="85" fill="var(--gold-light)" text-anchor="middle">النخيل</text>

      <!-- headline -->
      <text class="arabic headline" x="243" y="192" fill="url(#goldText)" text-anchor="middle" direction="rtl">الاختيار الأفضل</text>

      <!-- copy on bowl -->
      <text class="arabic tagline" x="245" y="484" fill="var(--gold)" text-anchor="middle" direction="rtl">من أجود أنواع البقوليات</text>
      <text class="latin from-nature" x="245" y="558" fill="var(--white)" text-anchor="middle">FROM NATURE</text>
      <text class="latin net-weight" x="240" y="594" fill="var(--white)" text-anchor="middle">1000gr</text>
      <circle cx="274" cy="590" r="5" fill="none" stroke="var(--white)" stroke-width="1"/>
      <line x1="269" y1="590" x2="279" y2="590" stroke="var(--white)" stroke-width="1"/>

      <!-- weight badge -->
      <g class="weight-badge-group">
        <circle cx="48" cy="636" r="33" fill="url(#goldBand)" stroke="var(--gold-dark)" stroke-width="1.5"/>
        <circle cx="48" cy="636" r="27" fill="none" stroke="var(--gold-dark)" stroke-width="1" stroke-dasharray="2 2"/>
        <text class="latin weight-badge" x="46" y="643" fill="var(--green-deep)" text-anchor="middle">5<tspan font-size="9" dy="-8">kg</tspan></text>
      </g>

      <!-- natural seal -->
      <g class="natural-seal">
        <circle cx="436" cy="636" r="34" fill="url(#goldBand)" stroke="var(--gold-dark)" stroke-width="1.5"/>
        <circle cx="436" cy="636" r="27" fill="none" stroke="var(--green-deep)" stroke-width="2"/>
      </g>
    </svg>
  </div>
</body>
</html>
```